Brightoak Business Card

Professional Business Card Design required using the attached contact information.

Contact information can be rearranged as required.

The company is a new start up venture developing solar systems, the branding should be in keeping with that of one of the investors whose website is as follows https://www.corvellan.com/

```html
<!DOCTYPE html>
<html lang="en">
<head>
<meta charset="utf-8">
<title>Brightoak Renewables – Business Card</title>
<link rel="stylesheet" href="https://fonts.googleapis.com/css2?family=Lato:wght@400;700&display=swap">
<style>
  :root {
    --stage: #3a332f;
    --card-dark: #2d323d;
    --card-light: #ffffff;
    --accent-green: #2a6a4e;
    --ink: #3b3b3b;
    --ink-strong: #111111;
    --muted: #6a6a6a;
    --on-dark: #e9ecef;
  }
  * { box-sizing: border-box; margin: 0; padding: 0; }
  html, body { width: 1200px; height: 795px; overflow: hidden; }
  body {
    background: var(--stage);
    font-family: "Lato", Arial, sans-serif;
    position: relative;
  }
  .card {
    position: absolute;
    top: 247px;
    width: 520px;
    height: 300px;
    border-radius: 4px;
    box-shadow: 0 10px 24px rgba(0,0,0,0.35);
    overflow: hidden;
  }
  .card--front { left: 50px; background: var(--card-dark); }
  .card--back { left: 630px; background: var(--card-light); }

  .wordmark {
    display: flex;
    align-items: center;
    gap: 10px;
    font-weight: 700;
    text-transform: uppercase;
    letter-spacing: 0.14em;
    white-space: nowrap;
  }
  .wordmark__dot {
    width: 8px; height: 8px; border-radius: 50%;
    background: var(--accent-green);
  }
  .card--front .wordmark {
    position: absolute;
    right: 40px;
    bottom: 40px;
    font-size: 15px;
    color: var(--on-dark);
  }
  .card--back .wordmark {
    position: absolute;
    left: 36px;
    top: 36px;
    font-size: 22px;
    color: var(--ink-strong);
  }

  .contact {
    position: absolute;
    left: 36px;
    top: 96px;
    color: var(--ink);
    font-size: 14px;
    line-height: 1.35;
  }
  .contact__name {
    color: var(--accent-green);
    font-size: 17px;
    font-weight: 700;
    text-transform: uppercase;
    letter-spacing: 0.02em;
  }
  .contact__role { color: var(--muted); margin-bottom: 12px; }
  .contact__address { margin-bottom: 12px; }
  .contact__line {
    display: flex;
    align-items: center;
    gap: 8px;
  }
  .contact__icon { width: 12px; height: 12px; flex: none; }
  .contact__icon path, .contact__icon circle, .contact__icon rect { fill: var(--accent-green); }
</style>
</head>
<body>

  <section class="card card--front" aria-label="Card front">
    <div class="wordmark">
      <span>Brightoak</span>
      <span class="wordmark__dot"></span>
      <span>Renewables</span>
    </div>
  </section>

  <section class="card card--back" aria-label="Card back">
    <div class="wordmark">
      <span>Brightoak</span>
      <span class="wordmark__dot"></span>
      <span>Renewables</span>
    </div>

    <div class="contact">
      <p class="contact__name">Daniel Hollis</p>
      <p class="contact__role">Founder &amp; CEO</p>
      <p class="contact__address">412 Marlowe Avenue<br>Boston, MA 02110</p>

      <p class="contact__line">
        <svg class="contact__icon" viewBox="0 0 12 12" aria-hidden="true">
          <path d="M2.5 1 L4.5 1 L5.3 3.5 L4 4.5 C4.6 5.9 6.1 7.4 7.5 8 L8.5 6.7 L11 7.5 L11 9.5 C11 10.3 10.3 11 9.5 11 C5 11 1 7 1 2.5 C1 1.7 1.7 1 2.5 1 Z"/>
        </svg>
        <span>+1 (555) 014-2276</span>
      </p>
      <p class="contact__line">
        <svg class="contact__icon" viewBox="0 0 12 12" aria-hidden="true">
          <path d="M1 2.5 H11 V9.5 H1 Z M1.6 3 L6 6.4 L10.4 3 Z" fill-rule="evenodd"/>
        </svg>
        <span>daniel.hollis@brightoak-renewables.com</span>
      </p>
      <p class="contact__line">
        <svg class="contact__icon" viewBox="0 0 12 12" aria-hidden="true">
          <circle cx="6" cy="6" r="5.2"/>
          <path d="M1 6 H11 M6 1 C4 3 4 9 6 11 M6 1 C8 3 8 9 6 11" stroke="#fff" stroke-width="0.8" fill="none"/>
        </svg>
        <span>www.corvellan.com</span>
      </p>
    </div>
  </section>

</body>
</html>
```